Label Design for Nuts package*

Develop the design for a label for nuts sold in a paperbag.

you can find our website here: www.brotkorn-snack.de.
Here comes the link to our catalogue: https://www.blattwerk-docs.com/de/document/read/48172095/brotkorn-premium-snacks-gesamtkatalog-2019

With this product we are targeting private customers who want to buy nuts with plastic free packaging online.
The colours of the label should fit the brown paper bag.

```html
<!DOCTYPE html>
<html lang="de">
<head>
<meta charset="utf-8">
<title>Brotkorn – Sonnenfund Etikett</title>
<link rel="stylesheet" href="https://fonts.googleapis.com/css2?family=Open+Sans:wght@700&family=Quicksand:wght@500;600;700&family=Roboto+Slab:wght@400&display=swap">
<style>
  :root {
    --navy: #0f1726;
    --sand: #d8c3a6;
    --cocoa: #6a3528;
    --cocoa-deep: #4f231b;
    --cocoa-light: #7a4233;
    --ring: #a39a8b;
    --gold: #cba67c;
    --tagline: #a8846a;
    --white: #ffffff;
  }
  html, body {
    margin: 0;
    padding: 0;
    width: 1090px;
    height: 1200px;
    overflow: hidden;
    background: var(--navy);
  }
  .label {
    display: block;
    width: 1090px;
    height: 1200px;
  }
  .brand-name {
    font-family: "Quicksand", sans-serif;
    font-weight: 500;
    font-size: 66px;
    letter-spacing: 6px;
    fill: var(--cocoa);
  }
  .brand-tagline {
    font-family: "Roboto Slab", serif;
    font-weight: 400;
    font-size: 21px;
    letter-spacing: 4px;
    fill: var(--tagline);
  }
  .product-name {
    font-family: "Open Sans", sans-serif;
    font-weight: 700;
    font-size: 78px;
    fill: var(--white);
  }
  .product-desc {
    font-family: "Quicksand", sans-serif;
    font-weight: 700;
    font-size: 45px;
    fill: var(--gold);
  }
  .net-weight {
    font-family: "Quicksand", sans-serif;
    font-weight: 700;
    font-size: 30px;
    fill: var(--white);
  }
</style>
</head>
<body>
<svg class="label" viewBox="0 0 1090 1200" xmlns="http://www.w3.org/2000/svg">
  <defs>
    <radialGradient id="nut-tones" cx="50%" cy="45%" r="60%">
      <stop offset="0%" stop-color="#b98558"/>
      <stop offset="55%" stop-color="#a8704a"/>
      <stop offset="100%" stop-color="#d9c09a"/>
    </radialGradient>
    <linearGradient id="seal-tone" x1="0" y1="0" x2="1" y2="1">
      <stop offset="0%" stop-color="var(--cocoa-light)"/>
      <stop offset="100%" stop-color="var(--cocoa-deep)"/>
    </linearGradient>
  </defs>

  <!-- background -->
  <rect class="label-base" width="1090" height="1200" fill="var(--navy)"/>

  <!-- sand band with brand -->
  <rect class="brand-band" x="213" y="0" width="667" height="480" fill="var(--sand)"/>
  <circle class="brand-dot" cx="545" cy="96" r="24" fill="var(--cocoa)"/>
  <text class="brand-name" x="545" y="222" text-anchor="middle">brotkorn</text>
  <text class="brand-tagline" x="545" y="260" text-anchor="middle">PREMIUM SNACKS</text>
  <line x1="394" y1="282" x2="696" y2="282" stroke="var(--tagline)" stroke-width="1.5"/>
  <circle cx="545" cy="282" r="5" fill="var(--sand)" stroke="var(--cocoa)" stroke-width="2"/>

  <!-- product window -->
  <circle class="window-ring" cx="545" cy="755" r="430" fill="var(--ring)"/>
  <circle class="window-photo" cx="545" cy="755" r="418" fill="url(#nut-tones)"
          role="img" aria-label="Foto einer gemischten Nussmischung aus Cashews, Mandeln, Haselnüssen, Walnüssen und Pistazien"/>

  <!-- product seal -->
  <rect class="weight-tab" x="407" y="860" width="277" height="340" fill="var(--cocoa)"/>
  <circle class="product-seal" cx="545" cy="755" r="322" fill="url(#seal-tone)"/>
  <circle cx="545" cy="755" r="318" fill="none" stroke="var(--cocoa-deep)" stroke-width="6" opacity="0.6"/>

  <text class="product-name" x="545" y="670" text-anchor="middle">Sonnenfund</text>
  <text class="product-desc" x="545" y="784" text-anchor="middle">ofengeröstete</text>
  <text class="product-desc" x="545" y="835" text-anchor="middle">cashewkerne</text>
  <text class="product-desc" x="545" y="885" text-anchor="middle">mit curry</text>

  <text class="net-weight" x="545" y="1140" text-anchor="middle">250gm</text>
</svg>
</body>
</html>
```